I need a business Card Design for my practice , i am clinical herbalist. I am a herbalist specializing in Lyme disease, autism, autoimmune diseases, difficult to cure diseasesDifficult to cure diseases. In my innovative practice i link traditional medicine, herbs with science, immunologu ,pharmacology.

Industry/Entity Type

Business

Contact Information for Business Card

My company name : OŚRODEK ZIELNIK
My name : Piotr Kaleta
Name of my profession : Fitoterapeuta
In Polish language Fitoterapeuta is Herbalist .

e-mail: piotrkaleta@osrodekzielnik.com
www.osrodek-zielnik.pl
phone : 604 587 231
My company adress : Dąbrowa Sitnicka 41 , 38-415 Lużna
I dont have logo .

Requirements
Nice to have
• My company

```html
<!DOCTYPE html>
<html lang="pl">
<head>
<meta charset="utf-8">
<title>Ośrodek Zielnik – wizytówka</title>
<link rel="stylesheet" href="https://fonts.googleapis.com/css2?family=Alfa+Slab+One&family=Montserrat+Alternates:wght@300;400;600&display=swap">
<style>
  :root {
    --backdrop: #7d8a90;
    --card: #000000;
    --teal: #148673;
    --teal-line: #1a9a86;
    --ink: #ffffff;
  }
  * { margin: 0; padding: 0; box-sizing: border-box; }
  html, body { width: 1200px; height: 900px; overflow: hidden; }
  body {
    background: var(--backdrop);
    font-family: "Montserrat Alternates", sans-serif;
    position: relative;
  }
  .business-card {
    position: absolute;
    left: 380px;
    top: 70px;
    width: 440px;
    height: 760px;
    background: var(--card);
    overflow: hidden;
  }
  .side-stripe {
    position: absolute;
    top: 0;
    bottom: 0;
    right: 38px;
    width: 18px;
    background: var(--teal);
  }
  .company-name {
    position: absolute;
    left: 38px;
    top: 70px;
    font-family: "Alfa Slab One", serif;
    color: var(--teal);
    font-size: 54px;
    line-height: 1.0;
    letter-spacing: -1px;
    transform: scaleX(0.86);
    transform-origin: left top;
  }
  .name-band {
    position: absolute;
    left: 0;
    top: 270px;
    width: 372px;
    height: 118px;
    background: var(--teal);
  }
  .name-band::after {
    content: "";
    position: absolute;
    right: -10px;
    top: -14px;
    width: 46px;
    height: 36px;
    background: var(--teal);
  }
  .person {
    position: absolute;
    right: 70px;
    top: 36px;
    text-align: left;
    color: var(--ink);
  }
  .person-name { font-size: 30px; font-weight: 600; line-height: 1.05; }
  .person-role { font-size: 14px; font-weight: 300; padding-left: 40px; }
  .contacts {
    position: absolute;
    right: 74px;
    top: 420px;
    width: 360px;
    color: var(--ink);
  }
  .contact-row {
    display: flex;
    justify-content: flex-end;
    align-items: flex-start;
    gap: 14px;
    margin-bottom: 52px;
  }
  .contact-text {
    text-align: right;
    font-weight: 400;
    font-size: 17px;
    line-height: 1.35;
  }
  .contact-text .small { font-size: 13px; }
  .contact-icon {
    flex: none;
    width: 46px;
    height: 46px;
    border: 2px solid var(--teal-line);
    background: var(--card);
    display: flex;
    align-items: center;
    justify-content: center;
  }
  .contact-icon svg { width: 24px; height: 24px; fill: none; stroke: var(--ink); stroke-width: 2.4; stroke-linecap: round; stroke-linejoin: round; }
  .contact-icon svg .solid { fill: var(--ink); stroke: none; }
</style>
</head>
<body>
  <main class="business-card">
    <div class="side-stripe"></div>

    <h1 class="company-name">OŚRODEK<br>ZIELNIK</h1>

    <section class="name-band">
      <div class="person">
        <div class="person-name">Piotr Kaleta</div>
        <div class="person-role">Fitoterapeuta</div>
      </div>
    </section>

    <section class="contacts">
      <div class="contact-row">
        <div class="contact-text">604 587 231</div>
        <div class="contact-icon" aria-label="telefon">
          <svg viewBox="0 0 24 24"><path class="solid" d="M6.6 3.5l3 3.2-1.8 2.1c1.2 2.6 3 4.4 5.5 5.6l2.1-1.8 3.2 3-2 3.1C10.6 18.3 5.7 13.4 3.6 5.5z"/></svg>
        </div>
      </div>
      <div class="contact-row">
        <div class="contact-text">
          <div class="small">piotrkaleta@osrodekzielnik.com</div>
          <div>www.osrodek-zielnik.pl</div>
        </div>
        <div class="contact-icon" aria-label="strona internetowa">
          <svg viewBox="0 0 24 24"><path d="M10 14a4 4 0 0 0 5.6 0l3-3a4 4 0 0 0-5.6-5.6l-1.2 1.2"/><path d="M14 10a4 4 0 0 0-5.6 0l-3 3a4 4 0 0 0 5.6 5.6l1.2-1.2"/></svg>
        </div>
      </div>
      <div class="contact-row">
        <div class="contact-text">
          <div>Dąbrowa Sitnicka 41</div>
          <div>38-415 Sitnica</div>
        </div>
        <div class="contact-icon" aria-label="adres">
          <svg viewBox="0 0 24 24"><path class="solid" d="M12 2.5a6.5 6.5 0 0 0-6.5 6.5c0 4.8 6.5 12.5 6.5 12.5s6.5-7.7 6.5-12.5A6.5 6.5 0 0 0 12 2.5zm0 9a2.5 2.5 0 1 1 0-5 2.5 2.5 0 0 1 0 5z"/></svg>
        </div>
      </div>
    </section>
  </main>
</body>
</html>
```